Brocure for Brindle - Social Media Management

Brindle is a Dutch company in the market of Social Media growth. We need a brochure (digital/PDF) for our company. Please see attached word doc for the text and attached logo. The initial proposal can contain just the first 4 pages text of the word doc.

We use informal language in all our communication.

Slogan: Effectieve Social Media Marketing voor professionals en ondernemers

Website: brindlesm-voorbeeld.nl

Industry/Entity Type

Digital Marketing

Contact Information for Business Card

Contact details:

Gerrit ter Hoeve
gerrit@brindlesm-voorbeeld.nl
06-19573826

```html
<!DOCTYPE html>
<html lang="nl">
<head>
<meta charset="utf-8">
<title>Brindle – Social Media Management brochure</title>
<link href="https://fonts.googleapis.com/css2?family=Montserrat:wght@400;500;600;700;800;900&family=Open+Sans:wght@400;600;700&display=swap" rel="stylesheet">
<style>
:root{
  --orange:#ef6a2a;
  --orange-soft:#f8b48a;
  --peach:#fdebe2;
  --navy:#1e2a46;
  --ink:#3d4250;
  --grey:#e6e6e6;
  --line:#b9bcc4;
  --teal-a:#2fa6dc;
  --teal-b:#56e0c9;
  --paper:#ffffff;
}
*{box-sizing:border-box;margin:0;padding:0}
html,body{width:1200px;height:2940px;overflow:hidden}
body{background:var(--grey);font-family:"Open Sans",sans-serif;color:var(--ink);position:relative}
.page{position:absolute;width:356px;height:505px;background:var(--paper);overflow:hidden}
.c1{left:172px}.c2{left:646px}
.r1{top:63px}.r2{top:639px}.r3{top:1213px}.r4{top:1785px}.r5{top:2361px}
.foot{position:absolute;left:20px;right:20px;bottom:17px;border-top:.6px solid var(--line);padding-top:3px;display:flex;justify-content:space-between;font-size:5px;color:var(--navy)}
.foot::after{content:"";position:absolute;right:0;bottom:-6px;width:30px;height:3px;background:var(--orange)}
.txt{font-size:4.9px;line-height:1.45;color:var(--ink)}
.txt p{margin-bottom:3px}
.h-orange{font-family:Montserrat,sans-serif;color:var(--orange);font-weight:600}
.h-navy{font-family:Montserrat,sans-serif;color:var(--navy);font-weight:800}
.art{position:absolute;border-radius:6px}
.wm{font-family:Montserrat,sans-serif;font-weight:700;color:var(--orange);display:flex;align-items:center;gap:4px}
.wm .dot{width:12px;height:12px;border-radius:50%;background:var(--orange)}

/* cover */
.cover{background:linear-gradient(160deg,#fdeee6 0%,#fff7f3 55%,#fff 100%)}
.cover .art{left:0;top:0;width:356px;height:300px;border-radius:0;background:radial-gradient(circle at 65% 45%,#5aa9e6 0,#8fc6ef 18%,#f6c2a5 40%,rgba(253,238,230,0) 70%)}
.cover-title{position:absolute;left:40px;top:290px;font-family:Montserrat,sans-serif;font-weight:900;font-size:15px;line-height:1;letter-spacing:.2px}
.cover-title span{display:block}
.cover-title .o{color:var(--orange)}.cover-title .n{color:var(--navy)}
.contact{position:absolute;left:40px;top:405px;border-left:1px solid var(--orange);padding-left:3px;font-size:5.2px;line-height:2;color:var(--navy);font-weight:600}
.site{position:absolute;left:40px;top:460px;font-family:Montserrat,sans-serif;font-weight:700;font-size:7.5px;color:var(--orange)}
.cover .wm{position:absolute;right:40px;top:447px;font-size:11px}

/* page 2 */
.p2 h1{position:absolute;left:40px;top:38px;font-size:11px;line-height:1.25;width:260px}
.p2 .sub{position:absolute;left:40px;top:74px;font-size:4.8px;font-weight:700;color:var(--navy);font-family:Montserrat,sans-serif}
.p2 .txt{position:absolute;left:40px;top:100px;width:276px}
.p2 .art{left:32px;top:185px;width:292px;height:170px;background:radial-gradient(ellipse at 65% 45%,#f6a77d 0,#fbd9c6 45%,#fff4ee 75%,#fff 100%)}
.formula{position:absolute;left:30px;top:420px;width:296px;text-align:center;font-size:6.4px;white-space:nowrap;color:var(--orange);font-family:Montserrat,sans-serif;font-weight:500}

/* page 3 */
.p3 .art1{left:22px;top:40px;width:92px;height:100px;background:radial-gradient(circle,#f28e55 0,#fbd2bb 50%,#fff 80%)}
.p3 .wie{position:absolute;left:158px;top:52px;width:170px}
.p3 .wie h2,.p3 .wat h2{font-size:10px;margin-bottom:8px}
.band{position:absolute;left:0;top:175px;width:356px;height:75px;background:var(--orange);clip-path:polygon(0 0,70% 0,74% 8%,100% 8%,100% 88%,68% 88%,64% 100%,0 100%)}
.band h2{position:absolute;left:40px;top:14px;font-family:Montserrat,sans-serif;font-weight:800;color:#fff;font-size:10px}
.band p{position:absolute;left:40px;top:36px;width:150px;font-size:4.8px;line-height:1.45;color:#fff}
.band .q-art{position:absolute;left:236px;top:10px;width:92px;height:52px;border-radius:6px;background:radial-gradient(ellipse at 50% 50%,#fff 0,#fcd9c4 40%,rgba(239,106,42,0) 75%)}
.p3 .art2{left:22px;top:285px;width:118px;height:170px;background:linear-gradient(180deg,#fff6dc 0,#e6efe5 55%,#9dbb9c 100%)}
.p3 .wat{position:absolute;left:158px;top:290px;width:170px}

/* page 4 */
.teal{position:absolute;left:0;top:48px;width:356px;height:138px;background:linear-gradient(90deg,var(--teal-a),var(--teal-b))}
.teal .tag{position:absolute;left:18px;top:-10px;background:var(--orange);color:#fff;font-family:Montserrat,sans-serif;font-weight:700;font-size:10.5px;padding:4px 10px 4px 12px;border-radius:0 3px 3px 0}
.teal .intro{position:absolute;left:30px;top:26px;font-size:4.6px;font-weight:700;color:#fff;line-height:1.35;font-family:Montserrat,sans-serif}
.teal ul{position:absolute;left:30px;top:52px;list-style:none;font-size:4.7px;color:#fff;line-height:2.55;font-weight:600}
.teal li::before{content:"";display:inline-block;width:5px;height:5px;border:.7px solid #fff;border-radius:50%;margin-right:9px;vertical-align:-1px}
.teal .art{left:200px;top:2px;width:150px;height:130px;background:radial-gradient(circle at 55% 55%,#f0f3f8 0,#b9c4d8 30%,rgba(255,255,255,0) 65%)}
.names{position:absolute;left:40px;top:237px;width:280px;display:flex;flex-wrap:wrap;gap:12px 24px;font-family:Montserrat,sans-serif;font-weight:700;font-size:11px;color:var(--navy)}
.waarom{position:absolute;left:40px;top:360px;width:112px;text-align:center}
.waarom h3{font-family:Montserrat,sans-serif;font-weight:800;font-size:9px;color:var(--navy);line-height:1.15}
.waarom .wm{justify-content:center;margin-top:8px;font-size:10px}
.waarom::after{content:"";position:absolute;right:-14px;top:0;height:72px;border-right:.7px solid var(--orange)}
.p4 .txt{position:absolute;left:170px;top:360px;width:150px}

/* page 5 */
.p5 .art{left:210px;top:165px;width:146px;height:230px;border-radius:6px 0 0 6px;background:linear-gradient(160deg,#f4f4f6,#dedfe4)}
.sect{position:absolute;left:40px}
.sect h4{font-family:Montserrat,sans-serif;color:var(--orange);font-size:5px;font-weight:700;margin-bottom:3px}

/* page 6 */
.p6 h2{position:absolute;left:90px;top:38px;font-size:11px}
.step{position:absolute;width:215px}
.step h4{font-family:Montserrat,sans-serif;color:var(--navy);font-weight:700;font-size:5.4px;margin-bottom:3px}

/* page 7 */
.p7 h2{position:absolute;left:40px;top:38px;font-size:11px}
.p7 .lead{position:absolute;left:40px;top:62px;width:220px}
.tbl{position:absolute;left:40px;top:98px;width:278px;display:grid;grid-template-columns:80px repeat(9,1fr);font-size:4.4px;border:.5px solid #d6d8de}
.tbl div{height:13.6px;display:flex;align-items:center;justify-content:center;border-bottom:.5px solid #e3e4e8;border-left:.5px solid #e3e4e8;background:#f4f5f7}
.tbl .lb{justify-content:flex-start;padding-left:6px;border-left:none;background:#fff;color:#666}
.tbl .sec{justify-content:flex-start;padding-left:4px;font-weight:700;color:var(--navy);background:#fff;grid-column:1 / -1;font-size:4.8px}
.tbl .hd{font-weight:700;color:var(--navy);flex-direction:column;height:18px;background:#fff;line-height:1.1}
.tbl i{width:6px;height:6px;border:.6px solid var(--orange);border-radius:1px;position:relative}
.tbl i::after{content:"";position:absolute;left:1.3px;top:.1px;width:2px;height:3.4px;border:solid var(--orange);border-width:0 .8px .8px 0;transform:rotate(40deg)}
.p7 .note{position:absolute;left:40px;top:415px;font-style:italic;font-size:4.8px}

/* page 8 & 10 */
.row{position:absolute;left:40px;width:280px;display:flex;gap:18px}
.ic{flex:none;width:24px;height:24px;border-radius:50%;background:var(--orange);display:flex;align-items:center;justify-content:center}
.row h4{font-family:Montserrat,sans-serif;color:var(--orange);font-weight:700;font-size:5px;margin-bottom:2px}
.row h5{font-size:5px;font-style:italic;color:var(--navy);margin-bottom:2px}
.row .txt{width:220px}
.p10 .row h4{color:var(--navy);font-size:5.4px}
.lic{flex:none;width:34px;height:30px;border:1px solid var(--navy);border-radius:3px;position:relative}
.lic::after{content:"";position:absolute;left:5px;right:5px;top:7px;height:2px;background:var(--orange);box-shadow:0 5px 0 var(--orange),0 10px 0 #c7cad1}

/* page 9 */
.p9 h2{position:absolute;left:40px;top:35px;font-size:11px}
.p9 .art{left:40px;top:60px;width:276px;height:230px;background:radial-gradient(circle at 50% 48%,#fde0cf 0,#fff3ec 45%,#fff 75%)}
.col{position:absolute;width:128px}
.col h4{font-family:Montserrat,sans-serif;color:var(--navy);font-weight:700;font-size:5.4px;margin-bottom:3px}
</style>
</head>
<body>

<!-- 1 cover -->
<section class="page c1 r1 cover">
  <div class="art" role="img" aria-label="Illustratie: hand met megafoon uit een smartphone waaruit kleurrijke social media iconen vliegen"></div>
  <h1 class="cover-title"><span class="o">EFFECTIEVE</span><span class="o">SOCIAL</span><span class="o">MEDIA</span><span class="o">MARKETING</span><span class="n">VOOR PROFESSIONALS</span><span class="n">EN ONDERNEMERS</span></h1>
  <div class="contact">Gerrit ter Hoeve<br>gerrit@brindlesm-voorbeeld.nl<br>06-19573826</div>
  <div class="site">www.brindlesm-voorbeeld.nl</div>
  <div class="wm"><span class="dot"></span>BRINDLE</div>
</section>

<!-- 2 intro -->
<section class="page c2 r1 p2">
  <h1 class="h-orange">Social Media Marketing voor zakelijke professionals en ondernemers</h1>
  <div class="sub">GROEI, INTERACTIE EN CONTENT</div>
  <div class="txt">
    <p>Je bereik vergroten, traffic genereren en daarmee meer omzet behalen. Dat is wat wij bieden.</p>
    <p>Onze services helpen jouw bereik op de sociale media te vergroten. Met een uitgebreide groeistrategie, onze kennis en geavanceerde tools zorgen we voor gerichte content en interactie op je sociale netwerken.</p>
  </div>
  <div class="art" role="img" aria-label="Illustratie: laptop met zwevende social media vensters en een doelwit met pijl"></div>
  <div class="formula">(actieve interactie + relevante content) &gt; actieve volgers) = (&gt; traffic + omzet)</div>
  <div class="foot"><span>Brindle - Social Media Management</span><span>www.brindlesm-voorbeeld.nl</span></div>
</section>

<!-- 3 wie -->
<section class="page c1 r2 p3">
  <div class="art art1" role="img" aria-label="Illustratie: smartphone met megafoon en social media iconen"></div>
  <div class="wie">
    <h2 class="h-navy">WIE ZIJN WIJ?</h2>
    <div class="txt"><p><b>Wij zijn Brindle.</b> Een team van sociale media experts dat je sociale netwerk activeert en het bereik vergroot. We zorgen voor sociale interactie met volgers, nieuwe en bestaande. Daarmee genereren we traffic naar je website/shop.</p>
    <p style="color:var(--orange);font-style:italic;font-weight:600">Het doel? Meer omzet. Simpel en heel meetbaar.</p></div>
  </div>
  <div class="band">
    <h2>VOOR WIE?</h2>
    <p>Onze dienstverlening kan ingezet worden op zowel persoonlijke zakelijke profielen (bv Netwerkly), of voor bedrijfspagina's op diverse sociale mediakanalen.</p>
    <div class="q-art" role="img" aria-label="Illustratie: drie witte ruimtelijke vraagtekens"></div>
  </div>
  <div class="art art2" role="img" aria-label="Illustratie: groeiende plant met social media iconen als bladeren en een zon"></div>
  <div class="wat">
    <h2 class="h-navy">WAT DOEN WE?</h2>
    <div class="txt">
      <p>Samen met jou bepalen we je doelen in de sociale netwerken. Zowel strategisch als tactisch en operationeel. Wij richten ons op die doelen en zorgen voor een netwerk van echte en actieve volgers.</p>
      <p>Of het nu gaat om Netwerkly, Beeldly, Vriendboek of Tjilp, interactie zorgt voor betrokken volgers. Die jij vervolgens in je verkoopproces kunt oppakken.</p>
      <p>Voor <b>zakelijke professionals</b> verzorgen wij personal branding met als doel impact en social sales. We zorgen voor veel meer relevante connecties en activeren je zakelijke netwerk. Gecombineerd met de juiste content strategie, zorgen wij ervoor dat je gezien wordt als autoriteit in je vakgebied.</p>
      <p>Onze diensten voor <b>bedrijven</b> bestaan uit de verschillende organische groei van het volgernetwerk, het activeren van het netwerk met content en interactie. We zorgen daarmee voor een groot bereik en verkeer naar je website.</p>
    </div>
  </div>
  <div class="foot"><span>Brindle - Social Media Management</span><span>www.brindlesm-voorbeeld.nl</span></div>
</section>

<!-- 4 platformen -->
<section class="page c2 r2 p4">
  <div class="teal">
    <div class="tag">Welke platformen?</div>
    <div class="intro">WE BIEDEN ONZE DIENSTEN AAN OP<br>ALLE BELANGRIJKE PLATFORMEN:</div>
    <ul>
      <li>Netwerkly (bedrijfspagina's en persoonlijke profielen)</li>
      <li>Vriendboek (bedrijfspagina's en groepen)</li>
      <li>Beeldly (bedrijfspagina's en persoonlijke profielen)</li>
      <li>Tjilp</li>
      <li>Kijkbuis</li>
      <li>Zoekplek Bedrijf</li>
      <li>Optioneel: Klipklap, Prikbord, Praathoek en Tuimel</li>
    </ul>
    <div class="art" role="img" aria-label="Illustratie: laptop met videoscherm en een opstijgende raket"></div>
  </div>
  <div class="names"><span>Netwerkly</span><span>Vriendboek</span><span>Beeldly</span><span>Tjilp</span><span>Kijkbuis</span><span>Zoekplek</span></div>
  <div class="waarom">
    <h3>WAAROM KIES<br>JE VOOR</h3>
    <div class="wm"><span class="dot"></span>BRINDLE</div>
  </div>
  <div class="txt">
    <p>Jij hebt jouw vak, wij het onze. Als iedereen doet waar hij goed in is, worden daar allemaal beter van. Wij zijn goed in het activeren en vergroten van je sociale netwerk. Daarvoor gebruiken we een slimme mix van kennis en tools.</p>
    <p>Een strategie die ervoor zorgt dat jij je kunt focussen op je corebusiness. Met onze slimme tools vergroten wij de impact van je sociale netwerken. Met als resultaat: meer traffic, meer leads, meer omzet.</p>
  </div>
  <div class="foot"><span>Brindle - Social Media Management</span><span>www.brindlesm-voorbeeld.nl</span></div>
</section>

<!-- 5 vragen -->
<section class="page c1 r3 p5">
  <div class="art" role="img" aria-label="Lijntekening: kantoorvoorwerpen, grafieken, lamp en dollartekens"></div>
  <div class="sect txt" style="top:38px;width:250px"><h4>DOEN WE ALLES ZELF?</h4><p>Wij zijn sterk in de strategie en systemen voor het vergroten van interactie. En we hebben een netwerk van specialisten die sterk zijn in hun vak. Zoals een reclamebureau, creatief ontwerper, websitebouwer of marketingstrategiebureau.</p><p style="font-style:italic">Is er op dat vlak een behoefte, dan brengen wij je graag in contact.</p></div>
  <div class="sect txt" style="top:95px;width:240px"><h4>HOE LANG GAAN WE MET ELKAAR IN ZEE?</h4><p>Een groeistrategie werkt op de lange termijn het beste als die groei organisch is. En dat vraagt dus ook een strategie voor de lange termijn. Lang is relatief, maar je moet erop rekenen dat we minimaal een jaar nodig hebben om de groeistrategie optimaal te laten werken. Natuurlijk is er in elke situatie snelle winst te behalen. Maar voor een goede samenwerking is het belangrijk dat je elkaar beter leert kennen en dat je regelmatig de koers bespreekt.</p></div>
  <div class="sect txt" style="top:163px;width:165px"><h4>GROEIEN OP SOCIALE MEDIA</h4><p>Het staat als een paal boven water: sociale media zijn een krachtig marketinginstrument. Een kans die je niet voorbij kunt laten gaan, of je dat nou leuk vindt of niet. Het geeft je de kans om je merk op te bouwen, je zicht- en vindbaarheid te verbeteren en uiteindelijk meer leads en verkopen te genereren. Om het beheren van je sociale platforms is een tijdrovende klus. En om resultaat te krijgen moet je het ook nog eens slim doen. Interactie, consistentie en responsiviteit zijn daarbij de sleutel.</p></div>
  <div class="sect txt" style="top:270px;width:165px"><h4>VOLLEDIG SOCIAAL MANAGEMENT</h4><p>We bieden een compleet beheerpakket voor sociale media waarmee we betrokkenheid van volgers realiseren en tijdig en altijd proactief schakelen naar de volgende stap. Zo blijven bezoekers geboeid en actief. We plannen zowel doelgroep- als branche specifieke inhoud en combineren online aanwezigheid om meer en meer gericht websiteverkeer te genereren.</p></div>
  <div class="sect txt" style="top:340px;width:165px"><h4>ACTIVEREN VAN JE NETWERK</h4><p>Je bent al een poos bezig met het beheren van je sociale media, maar ziet geen commercieel resultaat? De specialist maakt het verschil. Jouw kennis van jouw product en klant, gecombineerd met onze specialisme over sociale media, is zeer diverse branches. Wij gebruiken deze kennis voor een contentstrategie op maat.</p></div>
  <div class="sect txt" style="top:408px;width:276px"><h4>GROEISTRATEGIE</h4><p>Je netwerk op sociale media laten groeien kan een lastige klus zijn. Maar het levert je enorm veel op. Een groot aantal echte en actieve volgers geeft vertrouwen en genereert nog meer betrokkenheid. Het is de moderne variant van mond-tot-mondreclame. Wij hebben de expertise en oplossingen om al je profielen een echte boost te geven.</p><p style="font-style:italic">En wees voorbereid op groei!</p></div>
  <div class="foot"><span>Brindle - Social Media Management</span><span>www.brindlesm-voorbeeld.nl</span></div>
</section>

<!-- 6 hoe werkt het -->
<section class="page c2 r3 p6">
  <h2 class="h-orange">Hoe werkt het?</h2>
  <svg width="356" height="505" style="position:absolute;left:0;top:0" aria-hidden="true">
    <g fill="none" stroke="#8b8f99" stroke-width=".7" stroke-dasharray="2 2">
      <path d="M62 100 V128 H298 V150"/>
      <path d="M298 195 V215 H62 V233"/>
      <path d="M62 278 V300 H298 V318"/>
      <path d="M298 362 V382 H62 V398"/>
    </g>
    <g fill="#fff" stroke="#1e2a46" stroke-width="1">
      <polygon points="62,68 78,77 78,95 62,104 46,95 46,77"/>
      <polygon points="298,150 314,159 314,177 298,186 282,177 282,159"/>
      <polygon points="62,233 78,242 78,260 62,269 46,260 46,242"/>
      <polygon points="298,318 314,327 314,345 298,354 282,345 282,327"/>
      <polygon points="62,398 78,407 78,425 62,434 46,425 46,407"/>
    </g>
    <g fill="#ef6a2a"><circle cx="62" cy="86" r="5"/><circle cx="298" cy="168" r="5"/><circle cx="62" cy="251" r="5"/><circle cx="298" cy="336" r="5"/><circle cx="62" cy="416" r="5"/></g>
  </svg>
  <div class="step" style="left:90px;top:70px"><h4>Quick Scan &amp; advies</h4><div class="txt">We starten altijd met een grondige analyse van je website en sociale kanalen. Op basis daarvan geven we je een advies over de beste strategie.</div></div>
  <div class="step" style="left:90px;top:137px;width:180px"><h4>Je wilt met ons in zee</h4><div class="txt">Als je besluit met ons in zee te gaan, doen we dat met voor een paar weken. Want we doen niet aan hit-and-run, maar bouwen een samenwerking die op de lange termijn echte resultaten oplevert. We moeten elkaar goed leren kennen en dat vraagt tijd. Je vertrouwt ons je sociale mediakanalen toe. Dat vraagt vertrouwen en tegelijk moeten wij ons goed inleven in de manier van communicatie die past bij jouw business en jouw doelgroep.</div></div>
  <div class="step" style="left:90px;top:238px;width:180px"><h4>Pakketkeuze</h4><div class="txt">We hebben verschillende servicepakketten waaruit je kunt kiezen wat bij jouw situatie en wensen past. Blijkt op basis van de QuickScan dat je beter af bent met maatwerk, dan maken we daarvoor specifieke afspraken. Geen twee klanten zijn gelijk, daarom is ons aanbod flexibel opgebouwd.</div></div>
  <div class="step" style="left:90px;top:318px;width:180px"><h4>Implementatie</h4><div class="txt">Natuurlijk wil je zo snel mogelijk resultaat zien. Dat willen wij ook. We werken de strategie uit in een plan en gaan voor jou aan het werk. Met de prioriteit op die gebieden die zo snel mogelijk resultaten opleveren. Omdat we graag (leren) zien dat onze inspanningen verschil maken, starten we na een korte inwerkperiode. In het begin hebben we regelmatig overleg om elkaar goed te leren kennen.</div></div>
  <div class="step" style="left:90px;top:400px"><h4>Terugkoppeling en verbetering</h4><div class="txt">Iedere ondernemer is gedreven als het gaat om het behalen van resultaten. Zo ook wij. Wij doen er alles aan om onze dienstverlening zo succesvol mogelijk te laten zijn en jouw sociale doelen te behalen. We hebben regelmatig contact om de resultaten te bespreken.</div></div>
  <div class="foot"><span>Brindle - Social Media Management</span><span>www.brindlesm-voorbeeld.nl</span></div>
</section>

<!-- 7 tabel -->
<section class="page c1 r4 p7">
  <h2 class="h-navy">WAT DOEN WIJ:</h2>
  <div class="lead txt">Ze onderstaand overzicht met onze diensten en services, onder het overzicht beschrijven we de mogelijkheden.</div>
  <div class="tbl">
    <div class="hd lb"></div><div class="hd">NW<span>Page</span></div><div class="hd">NW<span>Profile</span></div><div class="hd">VB<span>Page</span></div><div class="hd">VB<span>Groep</span></div><div class="hd">VB<span>Profile</span></div><div class="hd">BL<span>Page</span></div><div class="hd">TJ<span>Page</span></div><div class="hd">KB<span>Page</span></div><div class="hd">ZB<span>Page</span></div>
    <div class="sec">Geagendeerdeposten</div>
    <div class="lb">Tekst/Fotoposts</div><div><i></i></div><div><i></i></div><div><i></i></div><div><i></i></div><div></div><div><i></i></div><div><i></i></div><div><i></i></div><div><i></i></div>
    <div class="lb">Tekst/Videoposts</div><div><i></i></div><div><i></i></div><div><i></i></div><div><i></i></div><div></div><div><i></i></div><div><i></i></div><div><i></i></div><div></div>
    <div class="sec">GroeiNetwerk</div>
    <div class="lb">Volgen/ontvolgen</div><div></div><div></div><div></div><div><i></i></div><div></div><div><i></i></div><div><i></i></div><div><i></i></div><div></div>
    <div class="lb">Vrienden/Connecties</div><div></div><div><i></i></div><div></div><div></div><div><i></i></div><div></div><div></div><div></div><div></div>
    <div class="sec">Interactie</div>
    <div class="lb">Posts/Likes</div><div><i></i></div><div><i></i></div><div><i></i></div><div><i></i></div><div><i></i></div><div><i></i></div><div><i></i></div><div><i></i></div><div></div>
    <div class="lb">Comments</div><div></div><div><i></i></div><div><i></i></div><div><i></i></div><div><i></i></div><div><i></i></div><div><i></i></div><div><i></i></div><div></div>
    <div class="sec">Berichten</div>
    <div class="lb">Mailing/bulk</div><div></div><div><i></i></div><div></div><div><i></i></div><div><i></i></div><div><i></i></div><div><i></i></div><div><i></i></div><div></div>
    <div class="lb">Autoantwoord</div><div></div><div><i></i></div><div></div><div><i></i></div><div><i></i></div><div><i></i></div><div><i></i></div><div></div><div></div>
    <div class="sec">Diversen</div>
    <div class="lb">Datamining</div><div><i></i></div><div><i></i></div><div><i></i></div><div><i></i></div><div><i></i></div><div><i></i></div><div><i></i></div><div><i></i></div><div></div>
    <div class="lb">Onderschrijven</div><div></div><div><i></i></div><div></div><div></div><div></div><div></div><div></div><div></div><div></div>
    <div class="lb">Uitnodigingspagina's</div><div></div><div><i></i></div><div></div><div></div><div><i></i></div><div><i></i></div><div><i></i></div><div><i></i></div><div></div>
    <div class="lb">Analyserapportage</div><div><i></i></div><div><i></i></div><div><i></i></div><div><i></i></div><div><i></i></div><div><i></i></div><div><i></i></div><div><i></i></div><div><i></i></div>
    <div class="lb">Contentmanagement</div><div><i></i></div><div><i></i></div><div><i></i></div><div><i></i></div><div><i></i></div><div><i></i></div><div><i></i></div><div><i></i></div><div><i></i></div>
    <div class="lb">SEO</div><div><i></i></div><div><i></i></div><div><i></i></div><div><i></i></div><div><i></i></div><div><i></i></div><div><i></i></div><div><i></i></div><div><i></i></div>
    <div class="lb">SEA</div><div><i></i></div><div><i></i></div><div><i></i></div><div><i></i></div><div><i></i></div><div><i></i></div><div><i></i></div><div><i></i></div><div></div>
    <div class="lb">Monitoring</div><div><i></i></div><div></div><div><i></i></div><div></div><div><i></i></div><div><i></i></div><div><i></i></div><div><i></i></div><div></div>
  </div>
  <div class="note">*Optioneel bieden wij diensten op Prikbord, Tuimel en Praathoek aan.</div>
  <div class="foot"><span>Brindle - Social Media Management</span><span>www.brindlesm-voorbeeld.nl</span></div>
</section>

<!-- 8 diensten -->
<section class="page c2 r4 p8">
  <div class="row" style="top:36px"><div class="ic"><svg width="12" height="12" viewBox="0 0 12 12" aria-hidden="true"><path d="M4 1v10M8 1v10M1 4h10M1 8h10" stroke="#fff" stroke-width="1.4"/></svg></div><div><h4>GEAGENDEERDE POSTEN</h4><div class="txt"><p>Geagendeerde posten is meer dan de voorbereiding van posts, het kiezen van de juiste hashtags en het redigeren van teksten. Per platform worden andere formaten van foto's en video's gevraagd. Wij zorgen ervoor dat ze voor ieder platform het juiste formaat hebben.</p><p>Daarnaast analyseren wij de posts en doelgroepen zodat we de berichten op het juiste moment van de dag plaatsen, voor het meeste effect en de meeste interactie met de doelgroep.</p></div></div></div>
  <div class="row" style="top:118px"><div class="ic"><svg width="12" height="12" viewBox="0 0 12 12" aria-hidden="true"><circle cx="5" cy="4" r="2" fill="#fff"/><path d="M1 10c0-3 8-3 8 0z" fill="#fff"/></svg></div><div><h4>GROEI NETWERK</h4><h5>Volgen / Ontvolgen</h5><div class="txt"><p>We zetten onze groeistrategie in op basis van locatie, hashtags, maar ook accounts van concurrenten en activiteit op deze accounts. Wij volgen relevante profielen, liken een post en wachten een paar dagen. Volgt het profiel ons niet terug, zullen we het ontvolgen en op de blocklist zetten.</p><p>We voorkomen zo dat profielen meerdere keren gevolgd worden. Zo bouwen we aan een nieuw volgersnetwerk dat we verder actief bewerken.</p></div></div></div>
  <div class="row" style="top:201px"><div class="ic"><svg width="12" height="12" viewBox="0 0 12 12" aria-hidden="true"><path d="M1 2h10v6H5l-3 3V8H1z" fill="#fff"/></svg></div><div><h4>INTERACTIE</h4><h5>Posts / Comments</h5><div class="txt"><p>We voorzien specifieke content van likes en/of commentaar. Hiervoor stellen we samen specifieke criteria en instellingen op. Zo zorgen we voor zichtbaarheid en interactie met de connecties, vrienden en volgers.</p></div></div></div>
  <div class="row" style="top:258px"><div class="ic"><svg width="12" height="12" viewBox="0 0 12 12" aria-hidden="true"><path d="M6 10.5L1.5 6A2.5 2.5 0 016 2.8 2.5 2.5 0 0110.5 6z" fill="#fff"/></svg></div><div><h4>VRIENDEN / CONNECTIES</h4><div class="txt"><p>Voor de groei op Netwerkly en Vriendboek gebruiken we een andere strategie, omdat een bijdrage weinig tot geen interactiemogelijkheden biedt. We gebruiken een 'persoonlijk' profiel waarmee we vrienden/connecties maken.</p><p>We gebruiken verschillende criteria zoals lidmaatschap van een groep, werkgebied in bepaalde industrie en dergelijke. Als de vriendschapsverzoeken zijn geaccepteerd, nodigen we deze personen uit om onze bedrijfspagina te volgen.</p></div></div></div>
  <div class="row" style="top:330px"><div class="ic"><svg width="12" height="12" viewBox="0 0 12 12" aria-hidden="true"><circle cx="6" cy="6" r="4.5" fill="none" stroke="#fff" stroke-width="1.2"/><path d="M3.5 6h5" stroke="#fff"/></svg></div><div><h4>BERICHTEN</h4><div class="txt"><p>Met behulp van berichten kunnen we volgers, vrienden en connecties benaderen. Niet alleen responsief, maar ook proactief. Zo kunnen we bijvoorbeeld een actie of specifieke content onder de aandacht brengen. In de meeste gevallen kunnen wij deze berichten personaliseren door bijvoorbeeld de voornaam te gebruiken.</p><p>Het is raadzaam dit spaarzaam in te zetten en zeker niet vaker dan eens per maand. Het doel en de toonzetting moeten passen binnen het netwerk.</p></div></div></div>
  <div class="row" style="top:402px"><div class="ic"><svg width="12" height="12" viewBox="0 0 12 12" aria-hidden="true"><rect x="1.5" y="2" width="9" height="6" rx="1" fill="#fff"/><path d="M4 8l-1 3 3-3" fill="#fff"/></svg></div><div><h4>AUTO ANTWOORD</h4><div class="txt"><p>Er kunnen verschillende soorten berichten automatisch worden verstuurd. Denk bijvoorbeeld aan een welkomstboodschap als een connectie- of vriendschapsverzoek is geaccepteerd.</p></div></div></div>
  <div class="foot"><span>Brindle - Social Media Management</span><span>www.brindlesm-voorbeeld.nl</span></div>
</section>

<!-- 9 diversen -->
<section class="page c1 r5 p9">
  <h2 class="h-orange">Diversen</h2>
  <div class="art" role="img" aria-label="Illustratie: centraal doelwit verbonden met schermen, smartphones, sterren en grafieken"></div>
  <div class="col txt" style="left:40px;top:305px"><h4>Datamining</h4><p>Alle acties die we uitvoeren, leveren data op. Die data verzamelen en registreren we. Op basis van zoekopdrachten kunnen we actief informatie binnenhalen, die we opslaan en op een andere wijze weer kunnen inzetten.</p><p>Als voorbeeld: we kunnen de Netwerkly-connectiedata (naam, email, telefoonnummer) binnenhalen en deze in bijvoorbeeld een CRM of mailingsysteem gebruiken.</p>
  <h4 style="margin-top:8px">Analyse en rapportage</h4><p>Vanuit onze systemen wordt bijgehouden wat de resultaten van de diverse campagnes en acties zijn. Deze analyses gebruiken we om de campagnes verder te optimaliseren en onze klanten te informeren.</p></div>
  <div class="col txt" style="left:188px;top:305px"><h4>Netwerkly interactie</h4><p>Iemands vaardigheden op Netwerkly bieden een waardevol contactmoment. Je kunt specifieke vaardigheden onderschrijven en toont daarmee dat je het profiel hebt bekeken. Het onderschrijven is een cadeautje voor de ontvanger. Vaak wordt er een - al dan niet standaard - bedankje gestuurd.</p><p>Dat bedankje biedt een opening voor een (commerciële) vraag. We kunnen een profiel van een connectie ook alleen 'bekijken', ook hiervan krijgt de connectie een melding.</p>
  <h4 style="margin-top:8px">Uitnodigen Pagina's</h4><p>Specifiek voor Vriendboek en Netwerkly kunnen we de gemaakte vrienden/connecties uitnodigen om de bedrijfspagina te liken/volgen.</p></div>
  <div class="foot"><span>Brindle - Social Media Management</span><span>www.brindlesm-voorbeeld.nl</span></div>
</section>

<!-- 10 content, seo -->
<section class="page c2 r5 p10">
  <div class="row" style="top:36px"><div class="lic"></div><div><h4>Content management</h4><div class="txt"><p>Content en posts kun je zelf maken of voorbereiden, maar wij kunnen dat ook voor je doen. Wij zijn gespecialiseerd in het selecteren van de meest effectieve woorden en hashtags voor jouw doelgroep. Dit is ook een belangrijk onderdeel voor het onderwerp 'zoekmachineoptimalisatie'.</p><p>Wij zorgen in ieder geval voor het agenderen en plaatsen van de posts. Wij bepalen de beste tijden per doelgroep op basis van onze ervaring en analyses. Per platform kunnen we zo de resultaten bijhouden en sturen.</p></div></div></div>
  <div class="row" style="top:122px"><div class="lic"></div><div><h4>Zoekmachineoptimalisatie (SEO)</h4><div class="txt"><p>Een fantastische marketingkans voor zowel grote als kleine bedrijven en organisaties is hoger in de zoekresultaten te verschijnen. Met een slimme SEO-strategie beïnvloeden we de vindbaarheid van je website in zoekmachines en genereren we waardevolle traffic naar je website - en daarmee nieuwe leads.</p><p>Dankzij de relatief lage investering en duurzaamheid van de resultaten, zijn wij er vast van overtuigd dat SEO centraal moet staan in je digitale marketingstrategie.</p></div></div></div>
  <div class="row" style="top:210px"><div class="lic"></div><div><h4>SEO voor lokale doelgroepen</h4><div class="txt"><p>Voor bedrijven met een fysiek bezoekadres is lokaal zoekverkeer ongelooflijk waardevol. Vaak zijn er veel minder middelen en dus investeringen nodig om effectief te scoren op deze zoekwoorden. We zijn zeer succesvol in het implementeren van lokale SEO-campagnes met een hoog investeringsrendement.</p><p>We combineren een uitgebreide analyse van je huidige online aanwezigheid met een grondig zoekwoordonderzoek. Zo optimaliseren we alle beschikbare factoren om de score van je website op de meest waardevolle zoektermen te verhogen.</p></div></div></div>
  <div class="row" style="top:310px"><div class="lic"></div><div><h4>Zoekwoorden advertenties (SEA)</h4><div class="txt"><p>Adverteren kan natuurlijk altijd. Maar met heeft onze voorkeur - afhankelijk van de fase waarin je sociale media zich bevinden - om organisch op een hoger plan te komen.</p><p>Wil je adverteren, dan kunnen wij dit volledig voor je verzorgen. Van het inregelen van de techniek, het maken van de advertenties, het selecteren van de zoekwoorden en het analyseren en verbeteren van de lopende ads-campagnes.</p></div></div></div>
  <div class="row" style="top:392px"><div class="lic"></div><div><h4>Monitoring</h4><div class="txt"><p>Met onze social media monitoringtools meten we zorgvuldig welke acties jouw doelgroep neemt en wat relevant is voor jouw bedrijf. Zo kom je er bijvoorbeeld achter welke opmerkingen je klanten geven over je producten en of er bepaalde klachten zijn.</p><p>Social media monitoring zorgt ervoor dat je hier snel op kunt anticiperen en reageren. Interactie met je klanten is offline, maar zeker online heel erg belangrijk!</p></div></div></div>
  <div class="foot"><span>Brindle - Social Media Management</span><span>www.brindlesm-voorbeeld.nl</span></div>
</section>

</body>
</html>
```